Graphic Design Project

Hi Designers
New Label for New Rum .
The label we would like is it to be modern and smart looking, simple and eye catching. Ingenuity is required and a great open mind to creating this label. Type of rum -Rich flavour with a smooth rounded character. It has robust fruity flavours of molasses, honey and chocolate and is not as sweet as other rums, giving it a strong dark rum taste for the "real rum drinker. If you google Copper Tide Rum thats the type of bottle using .
Name is : Marlowe Amber
Size:1l
Alcohol :37.5% Imported Dark Rum
Final designer will be paid extra for posters and t shirt designs. email is devan@tolvik.co.nz
Target Market(s)
Rum Drinkers .
Industry/Entity Type
Graphic Design
Look and feel
Each slider illustrates characteristics of the customer's brand and the style your logo design should communicate.

```html
<!DOCTYPE html>
<html lang="en">
<head>
<meta charset="utf-8">
<title>Marlowe Amber – Imported Dark Rum Label</title>
<link rel="stylesheet" href="https://fonts.googleapis.com/css2?family=Fredoka:wght@600&family=Lato:wght@400&display=swap">
<style>
  :root {
    --backdrop: #e6e6e8;
    --label-edge: #e8701c;
    --label-glow: #ffe37e;
    --label-mid: #f59a34;
    --label-border: #c9641e;
    --emblem: #1c1a1e;
    --name: #d9461a;
    --subline: #c41a2e;
  }
  html, body {
    margin: 0;
    padding: 0;
    width: 1200px;
    height: 2439px;
    overflow: hidden;
    background: var(--backdrop);
  }
  .canvas {
    position: relative;
    width: 1200px;
    height: 2439px;
  }
  .label {
    position: absolute;
    left: 50px;
    top: 136px;
    width: 1100px;
    height: 2166px;
    box-sizing: border-box;
    border: 4px solid var(--label-border);
    background: radial-gradient(ellipse 62% 42% at 50% 40%, var(--label-glow) 0%, var(--label-mid) 48%, var(--label-edge) 100%);
  }
  .label__emblem {
    position: absolute;
    left: 50%;
    top: 520px;
    width: 520px;
    height: 520px;
    margin-left: -260px;
    border-radius: 50%;
    background: var(--emblem);
  }
  .label__name {
    position: absolute;
    left: 0;
    right: 0;
    top: 1600px;
    margin: 0;
    text-align: center;
    font-family: "Fredoka", "Arial Rounded MT Bold", sans-serif;
    font-weight: 600;
    font-size: 118px;
    letter-spacing: 2px;
    text-transform: uppercase;
    color: var(--name);
    line-height: 1;
  }
  .label__type {
    position: absolute;
    left: 0;
    right: 0;
    top: 1915px;
    margin: 0;
    text-align: center;
    font-family: "Lato", "Helvetica", sans-serif;
    font-size: 58px;
    color: var(--subline);
    line-height: 1;
  }
  .label__strength {
    position: absolute;
    left: 0;
    right: 0;
    top: 2000px;
    margin: 0;
    text-align: center;
    font-family: "Lato", "Helvetica", sans-serif;
    font-size: 42px;
    color: var(--subline);
    line-height: 1;
  }
</style>
</head>
<body>
  <main class="canvas">
    <section class="label">
      <div class="label__emblem" aria-hidden="true"></div>
      <h1 class="label__name">Marlowe Amber</h1>
      <p class="label__type">Imported Dark Rum</p>
      <p class="label__strength">37.5% ALC./VOL.</p>
    </section>
  </main>
</body>
</html>
```